Hal's Remedies Business Card Design Project

I need a business card designed for my pharmacy Hal's Remedies. I would like just the logo on one side, maybe with black background and white lettering. The other side I would also like to include my logo which is attached. Also, please include my name and the following information:
Hal Norwick Owner/Pharm D.
Business address is 7163 N Birch Rd Sioux Falls, SD 57291.
Phone number is 605-318-6027 and fax # is 605-318-6031.
my email address is hal@halsremedies.example.
My website is www.halsremedies.example.
My business hours are Monday-Friday 8am-7 pm. Saturday 8am-12 pm. Sunday Closed.
I would like the design to include my logo colors, black, white, and neon green. Silver may be added as a highlight. Thanks.
Pharmacy
See above in product description

```html
<!DOCTYPE html>
<html lang="en">
<head>
<meta charset="utf-8">
<title>Hal's Remedies – Business Card</title>
<link rel="stylesheet" href="https://fonts.googleapis.com/css2?family=Ubuntu:wght@400;500;700&display=swap">
<style>
  :root {
    --page: #ffffff;
    --card: #252525;
    --ink: #ffffff;
    --accent: #a6c817;
    --divider: #d9d9d9;
  }
  * { margin: 0; padding: 0; box-sizing: border-box; }
  html, body {
    width: 1200px;
    height: 361px;
    overflow: hidden;
    background: var(--page);
    font-family: "Ubuntu", sans-serif;
    color: var(--ink);
  }
  .sheet { position: relative; width: 1200px; height: 361px; }
  .card {
    position: absolute;
    top: 16px;
    width: 574px;
    height: 328px;
    background: var(--card);
  }
  .card--front { left: 16px; }
  .card--back { left: 604px; }

  /* Front: centred brand name */
  .front-brand {
    position: absolute;
    inset: 0;
    display: flex;
    align-items: center;
    justify-content: center;
    gap: 18px;
  }
  .front-brand__dot {
    width: 26px; height: 26px;
    border-radius: 50%;
    background: var(--accent);
  }
  .front-brand__name {
    font-size: 44px;
    font-weight: 500;
    letter-spacing: -0.5px;
    color: var(--ink);
  }

  /* Back: header brand */
  .back-brand {
    position: absolute;
    left: 34px;
    top: 34px;
    display: flex;
    align-items: center;
    gap: 12px;
  }
  .back-brand__dot {
    width: 14px; height: 14px;
    border-radius: 50%;
    background: var(--accent);
  }
  .back-brand__rule {
    width: 1px; height: 46px;
    background: var(--divider);
  }
  .back-brand__name {
    font-size: 22px;
    font-weight: 500;
    letter-spacing: -0.3px;
  }

  .contact {
    position: absolute;
    left: 32px;
    top: 99px;
    font-size: 16px;
    line-height: 22px;
  }
  .contact__name { font-size: 21px; line-height: 24px; }
  .contact__role { color: var(--accent); margin-top: 2px; margin-bottom: 7px; }
  .contact__phones { margin-top: 6px; }
  .label { color: var(--accent); font-weight: 700; }

  .hours {
    position: absolute;
    right: 42px;
    top: 180px;
    text-align: right;
    font-size: 16px;
    line-height: 22px;
  }
  .web {
    position: absolute;
    right: 42px;
    top: 260px;
    text-align: right;
    font-size: 16px;
    line-height: 21px;
  }
  .web__url { color: var(--accent); font-weight: 700; }
</style>
</head>
<body>
<main class="sheet">
  <section class="card card--front" aria-label="Card front">
    <div class="front-brand">
      <span class="front-brand__dot"></span>
      <span class="front-brand__name">Hal's Remedies</span>
    </div>
  </section>

  <section class="card card--back" aria-label="Card back">
    <header class="back-brand">
      <span class="back-brand__dot"></span>
      <span class="back-brand__rule"></span>
      <span class="back-brand__name">Hal's Remedies</span>
    </header>

    <div class="contact">
      <p class="contact__name">Hal Norwick</p>
      <p class="contact__role">Owner/Pharm D.</p>
      <address class="contact__address" style="font-style:normal">
        7163<br>N Birch Rd<br>Sioux Falls<br>SD 57291
      </address>
      <p class="contact__phones">
        <span class="label">t:</span> 605-318-6027<br>
        <span class="label">f:</span> 605-318-6031
      </p>
    </div>

    <div class="hours">
      <p>Monday-Friday: 8am-7 pm</p>
      <p>Saturday: 8am-12 pm</p>
      <p>Sunday: Closed</p>
    </div>

    <div class="web">
      <p><span class="label">e:</span> hal@halsremedies.example</p>
      <p class="web__url">www.halsremedies.example</p>
    </div>
  </section>
</main>
</body>
</html>
```